Web Design Project

Dear designer(s),

I need a design for a shop who's specialized into...

-Material to fix or do tailor made clothing (cloth, buttons, zippers etc)
-Curtains (static/pull-up)
-Blinds (plastic/wood)

that kind of stuff.

Good thing is that I can provide a lot of pretty photo's to work with. I have 3.5 Gigabyte of 300-1200 dpi photo's altho I converted most of them to 72dpi for your convenience (75Mb).

You can download the working material from this quellbin link:

http://files.quellbin.net/u/31920586/Velunor.zip

this is an updated file, it contains the dutch menu items to use in your design

http://files.quellbin.net/u/31920586/Velunor_Content.txt

Notice: take your time to come up with something nice. I prefer 1 or 2 designs from a designer that has been thinked of, than 5 quick ones.
Updates

Thank you for those who posted designs already but I want to clarify something.

As I mentioned it's a shop, that's a physical shop and not a webshop.

So you can safe some time and skip drawing the shopping cart icons, shop items on the homepage and other shop related things.

They don't want to start online reselling as they already spend most of their time in their shop to catch up with all orders.

Keep up the good work!

Industry/Entity Type

Clothing

Requirements
Nice to have
• Maybe the hi-res pictures can be used as background ratotor that appears left/right next to the centered website content?

Since there is a lot of material each section might have his topic linked set of thumbnails that opens a bigger image on clicking?

```html
<!DOCTYPE html>
<html lang="en">
<head>
<meta charset="utf-8">
<title>Velunor – Home</title>
<link rel="stylesheet" href="https://fonts.googleapis.com/css2?family=Roboto+Condensed:wght@300;400&display=swap">
<style>
  :root {
    --blue: #0a7ac6;
    --blue-panel: rgba(30, 130, 200, 0.88);
    --blue-dark: #0b3e66;
    --grey-dark: #5e5e5e;
    --page-bg: #efefef;
    --text-dark: #555555;
    --text-muted: #8a8a8a;
    --white: #ffffff;
  }
  * { box-sizing: border-box; margin: 0; padding: 0; }
  html, body { width: 1200px; height: 1118px; overflow: hidden; }
  body {
    position: relative;
    background: var(--page-bg);
    font-family: "Roboto Condensed", "Arial Narrow", sans-serif;
    color: var(--text-dark);
  }
  .hero {
    position: absolute; left: 0; top: 0; width: 1200px; height: 811px;
    background:
      radial-gradient(ellipse at 45% 55%, #d9d3cb 0%, rgba(217,211,203,0) 45%),
      radial-gradient(ellipse at 85% 40%, #d6cfa0 0%, rgba(214,207,160,0) 25%),
      linear-gradient(90deg, #e3e3e1 0%, #ebe8e3 40%, #e6e0d8 70%, #d8cfc4 100%);
  }
  .hero-rule {
    position: absolute; left: 0; top: 811px; width: 1200px; height: 4px;
    background: var(--blue);
  }
  .sidebar {
    position: absolute; left: 131px; top: 76px; width: 253px; height: 456px;
    background: var(--blue-panel);
    border-top: 7px solid #3a92d0;
  }
  .brand {
    height: 109px; background: var(--white);
    display: flex; flex-direction: column; justify-content: center;
    padding-left: 23px;
  }
  .brand-name { font-size: 26px; color: var(--blue); font-weight: 400; line-height: 1; }
  .brand-url { font-size: 13px; color: var(--text-muted); margin-top: 6px; margin-left: 100px; }
  .main-nav { list-style: none; margin-top: 77px; }
  .main-nav li {
    height: 33px; line-height: 31px; padding-left: 30px;
    font-size: 15px; color: var(--white); text-transform: uppercase;
  }
  .main-nav li.active { background: var(--blue-dark); }
  .main-nav li.contact { margin-top: 4px; }
  .gallery {
    position: absolute; left: 131px; top: 636px; width: 939px; height: 115px;
    background: rgba(245, 245, 245, 0.82);
  }
  .gallery-track {
    position: absolute; left: 49px; top: 14px; width: 843px; height: 87px; overflow: hidden;
  }
  .thumb { position: absolute; top: 0; width: 144px; height: 87px; }
  .gallery-arrow { position: absolute; top: 48px; }
  .welcome {
    position: absolute; left: 130px; top: 843px; width: 639px; height: 234px;
    border-top: 5px solid var(--blue);
  }
  .projects {
    position: absolute; left: 769px; top: 843px; width: 301px; height: 234px;
    border-top: 5px solid var(--grey-dark);
  }
  .panel-title {
    height: 44px; background: var(--white); padding-left: 13px;
    font-size: 28px; font-weight: 300; line-height: 44px; color: var(--text-dark);
  }
  .panel-title .accent { color: var(--blue); }
  .welcome-body {
    height: 185px; background: var(--blue); color: var(--white);
    padding: 9px 14px 0 13px; font-size: 12.5px; line-height: 16px; position: relative;
  }
  .welcome-body p + p { margin-top: 15px; }
  .projects-body { height: 185px; background: var(--grey-dark); position: relative; }
  .project-frame {
    position: absolute; left: 13px; top: 14px; width: 275px; height: 99px;
    border: 1px solid #8a8a8a; padding: 7px;
  }
  .project-image { width: 259px; height: 85px; }
  .read-more {
    position: absolute; top: 142px; width: 74px; height: 26px;
    background: var(--white); font-size: 14px; line-height: 26px; text-align: right;
    padding-right: 6px;
  }
  .read-more::before {
    content: ""; position: absolute; left: 0; top: 8px;
    border-left: 6px solid transparent; border-top: 5px solid transparent; border-bottom: 5px solid transparent;
  }
  .welcome .read-more { right: 18px; color: var(--blue); }
  .welcome .read-more::before { border-left-color: var(--blue); }
  .projects .read-more { right: 14px; color: var(--text-dark); }
  .projects .read-more::before { border-left-color: var(--grey-dark); }
  .footer-nav {
    position: absolute; left: 131px; top: 1094px; display: flex; list-style: none;
    font-size: 11px; color: var(--text-muted); text-transform: uppercase;
  }
  .footer-nav li + li::before { content: "|"; margin: 0 9px; color: #c8c8c8; font-size: 8px; vertical-align: 2px; }
  .copyright {
    position: absolute; right: 130px; top: 1090px;
    font-size: 14px; color: var(--text-muted); text-transform: uppercase;
  }
</style>
</head>
<body>
  <div class="hero" role="img" aria-label="Photo of a bright living room with a cream sofa, fur throw, floor lamp, blinds and flowers"></div>
  <div class="hero-rule"></div>

  <aside class="sidebar">
    <div class="brand">
      <span class="brand-name">Velunor</span>
      <span class="brand-url">www.velunor.be</span>
    </div>
    <ul class="main-nav">
      <li class="active">Home</li>
      <li>Tafellinnen</li>
      <li>Decoration cloth</li>
      <li>Optreksystemen</li>
      <li class="contact">Contact us</li>
    </ul>
  </aside>

  <section class="gallery">
    <svg class="gallery-arrow" style="left:19px" width="14" height="22" viewBox="0 0 14 22"><polyline points="12,1 2,11 12,21" fill="none" stroke="#5a9fd6" stroke-width="2"/></svg>
    <div class="gallery-track">
      <div class="thumb" style="left:0;background:linear-gradient(180deg,#c9d8e2,#e6e9ea 60%,#8c959a)" role="img" aria-label="Kitchen with blue blinds"></div>
      <div class="thumb" style="left:151px;background:linear-gradient(180deg,#dcdcd8,#ece9e2 55%,#b8aea2)" role="img" aria-label="Attic room with white sofa"></div>
      <div class="thumb" style="left:303px;background:linear-gradient(180deg,#e4e6e6,#f0f0ef 60%,#9a9c9c)" role="img" aria-label="White living room with black chairs"></div>
      <div class="thumb" style="left:455px;background:linear-gradient(180deg,#e3b49c,#c6b9a8 50%,#6f6a66)" role="img" aria-label="Living room with roman blinds and lamp"></div>
      <div class="thumb" style="left:607px;background:linear-gradient(180deg,#d9d5cf,#a99686 50%,#5d5650)" role="img" aria-label="Dining room with brown blinds"></div>
      <div class="thumb" style="left:758px;background:linear-gradient(180deg,#e4e6e6,#f0f0ef 60%,#9a9c9c)" role="img" aria-label="White living room with black chairs"></div>
    </div>
    <svg class="gallery-arrow" style="left:911px" width="14" height="22" viewBox="0 0 14 22"><polyline points="2,1 12,11 2,21" fill="none" stroke="#5a9fd6" stroke-width="2"/></svg>
  </section>

  <section class="welcome">
    <h2 class="panel-title">Welcome To <span class="accent">Velunor</span></h2>
    <div class="welcome-body">
      <p>Lorem ipsum dolor sit amet, consectetuer adipiscing elit, sed diam nonummy nibh euismod tincidunt ut laoreet dolore magna aliquam erat volutpat. Ut wisi enim ad minim veniam.Lorem ipsum dolor sit amet, consectetuer adipiscing elit, sed diam nonummy nibh euismod tincidunt ut laoreet dolore magna aliquam erat volutpat.</p>
      <p>Lorem ipsum dolor sit amet, consectetuer adipiscing elit, sed diam nonummy nibh euismod tincidunt ut laoreet dolore magna aliquam erat volutpat. Ut wisi enim ad minim veniam.Lorem ipsum dolor sit amet, consectetuer adipiscing elit, sed diam nonummy nibh euismod tincidunt ut laoreet dolore magna aliquam erat volutpat.</p>
      <a class="read-more">Read More</a>
    </div>
  </section>

  <section class="projects">
    <h2 class="panel-title">Latest Projects</h2>
    <div class="projects-body">
      <div class="project-frame">
        <div class="project-image" style="background:linear-gradient(180deg,#e3b49c,#c6b9a8 50%,#6f6a66)" role="img" aria-label="Living room with roman blinds, lamp and sofa"></div>
      </div>
      <a class="read-more">Read More</a>
    </div>
  </section>

  <ul class="footer-nav">
    <li>Home</li>
    <li>Tafellinnen</li>
    <li>Decoration cloth</li>
    <li>Optreksystemen</li>
    <li>Contact</li>
  </ul>
  <p class="copyright">Velunor © 2013, All rights reserved.</p>
</body>
</html>
```